Real Estate | Property Management Website Design

We are working with a Real Estate company in California. They provide Property Management Services and Real Estate Services.

PLEASE NOT: make sure the site covers real estate and property management).

A few websites for inspiration:
https://brimcastleleasing.example
https://www.harborvaleestates.example
https://morvenaltiski.example
https://tobelnashridge.example
https://theosterlundteam.example
https://brennaholtcamp.example
https://zvenhaus.example

Thank you for taking the time to consider designing a website for us. We are web developers based in Stockton, CA, USA. Most of our projects go through the same process. Understanding this process may help you win a project with us. We custom-code all of our websites in-house. We don’t have any requirements as to what tools you use for your design, but we ask that you follow these guidelines.

IMAGES:
If you use any images or icons in the design, we ask that you have a link to the asset so we can purchase the image/icon. Most of the designs we submit do not have the customer’s images on them unless they have some great images. Be creative; show us the feeling you are trying to portray with your image choices. Use any royalty-free site you choose. We subscribe to Quillory and mainly use their images, but we can purchase images outside of Quillory. PLEASE NOTE: we will not submit designs to clients with watermarks on the images.

FONTS:
We ask that you identify the fonts you’re using in the design. This can be done in a message if you want. We typically use Vantrel Fonts and Quillory Fonts.

CONTENT:
We're always open to different content and ideas. We often submit designs with stock images so the client can see our vision. We typically take pictures after the website launch to use their images with our vision. Lorem Ipsum is fine for paragraphs, but we ask that you make the Headers with correct English. We want to be able to show the vision and identify the sections of the website.

INSPIRATION:
We typically add a couple of links in the brief of websites we like to help you get started in your design.

REVISIONS:
We do not often ask for revisions of the designs unless we see something in the design that may not appeal to the client. If there are slight changes that we want to make, we do that in the development process.

FEEDBACK:
We rarely give feedback on designs during the design process. We are working on many website projects and do not have the time to provide feedback. We usually respond if your request is well thought out and asks specific questions, but a note asking “feedback, please” usually goes unanswered.

```html
<!DOCTYPE html>
<html lang="en">
<head>
<meta charset="utf-8">
<title>Larkmoor Properties</title>
<link href="https://fonts.googleapis.com/css2?family=Outfit:wght@400;500;600;700&family=Roboto:wght@400;500;700&display=swap" rel="stylesheet">
<style>
:root{
  --orange:#f26b21;
  --orange-light:#ff8a3d;
  --ink:#1e1e1e;
  --text:#555555;
  --peach:#fcece5;
  --dark:#1b1b1b;
  --white:#ffffff;
  --line:#3a3a3a;
}
*{box-sizing:border-box;margin:0;padding:0}
html,body{width:1200px;height:4367px;overflow:hidden}
body{position:relative;font-family:'Roboto',sans-serif;color:var(--text);background:var(--white)}
.abs{position:absolute}
.heading{font-family:'Outfit',sans-serif;color:var(--ink);font-weight:600}
.accent{color:var(--orange)}
.btn{position:absolute;display:flex;align-items:center;justify-content:center;gap:8px;background:var(--orange);color:var(--white);font-family:'Roboto',sans-serif;font-weight:500;font-size:14px;border-radius:30px;text-transform:uppercase}
.btn-outline{background:var(--white);color:var(--orange);border:1.5px solid var(--orange)}
.arrow{width:13px;height:13px}
.photo{position:absolute;overflow:hidden}

/* header */
.site-header{position:absolute;left:0;top:0;width:1200px;height:117px;background:var(--white)}
.brand{position:absolute;left:51px;top:30px;display:flex;align-items:center;gap:14px}
.brand-mark{width:52px;height:52px;background:var(--orange)}
.brand-name{font-family:'Outfit',sans-serif;font-weight:700;font-size:30px;line-height:1;color:var(--orange);letter-spacing:1px}
.socials{position:absolute;left:712px;top:17px;display:flex;gap:8px}
.social{width:32px;height:32px;border:1.5px solid var(--orange);border-radius:50%}
.top-phone{position:absolute;left:886px;top:17px;display:flex;align-items:center;gap:12px;font-family:'Outfit',sans-serif;font-weight:600;font-size:20px;color:var(--ink)}
.phone-badge{width:36px;height:32px;border-radius:16px;background:#f1f1f1;display:flex;align-items:center;justify-content:center}
.nav{position:absolute;left:356px;top:68px;width:844px;height:49px;background:var(--orange);clip-path:polygon(28px 0,100% 0,100% 100%,0 100%)}
.nav a{position:absolute;top:15px;color:var(--white);font-size:14px;text-decoration:none;text-transform:uppercase}
.nav .sep{position:absolute;top:14px;color:var(--white);font-size:14px}

/* hero */
.hero{position:absolute;left:0;top:117px;width:1200px;height:664px;background:linear-gradient(100deg,#6b4a33 0%,#a57e5e 30%,#c9b29c 55%,#9a8c80 100%)}
.hero-shade{position:absolute;inset:0;background:linear-gradient(90deg,rgba(0,0,0,0) 35%,rgba(0,0,0,.35) 100%)}
.hero-copy{position:absolute;left:580px;top:210px;color:var(--white)}
.hero-kicker{font-family:'Outfit',sans-serif;font-weight:600;font-size:33px;line-height:1}
.hero-title{font-family:'Outfit',sans-serif;font-weight:700;font-size:46px;line-height:1;margin-top:22px;white-space:nowrap}
.hero-text{font-size:16px;line-height:27px;margin-top:20px;width:440px}

/* services */
.section-title{position:absolute;left:0;width:1200px;text-align:center;font-family:'Outfit',sans-serif;font-weight:600;font-size:36px;color:var(--ink)}
.service-title{position:absolute;font-family:'Outfit',sans-serif;font-weight:500;font-size:34px;line-height:41px;color:var(--ink)}
.service-text{position:absolute;font-size:14px;line-height:25.6px;color:var(--text)}
.service-icon{position:absolute;width:120px;height:120px;border-radius:50%;border:2.5px dotted var(--orange);background:var(--white);display:flex;align-items:center;justify-content:center}
.service-icon span{width:92px;height:92px;border-radius:50%;background:linear-gradient(135deg,#f58a43,#d9531a);display:flex;align-items:center;justify-content:center}

/* about */
.about{position:absolute;left:0;top:1922px;width:1200px;height:571px;background:var(--peach)}
.about-text{position:absolute;left:114px;top:157px;width:492px;font-size:15px;line-height:25.8px;color:#444;text-align:justify}
.circle-photo{position:absolute;border-radius:50%;border:5px solid var(--white);box-shadow:0 4px 14px rgba(0,0,0,.12)}

/* testimonials */
.testimonials{position:absolute;left:0;top:2493px;width:1200px;height:531px;background:linear-gradient(180deg,#f5762d,#f47a35 60%,#f58a4c)}
.testimonials .section-title{color:var(--white);top:85px}
.t-card{position:absolute;top:170px;width:308px;height:264px;background:var(--white);text-align:center;box-shadow:0 6px 16px rgba(0,0,0,.12)}
.avatar{width:84px;height:84px;border-radius:50%;margin:32px auto 0;background:linear-gradient(180deg,#d9d9d9,#9aa6b0);border:3px solid #eee}
.quote-mark{position:absolute;font-family:Georgia,serif;font-size:60px;color:#d6d6d6;line-height:1}
.t-text{position:relative;z-index:1;margin:28px auto 0;width:250px;font-size:15px;line-height:25.5px;color:#333}
.t-name{position:relative;z-index:1;margin-top:8px;font-size:15px;font-weight:500;color:var(--orange)}

/* blog */
.blog-grid{position:absolute;left:114px;top:3180px;width:972px;height:576px;box-shadow:0 2px 14px rgba(0,0,0,.1);display:grid;grid-template-columns:repeat(3,324px);grid-template-rows:288px 288px;background:var(--white)}
.post{position:relative;padding:38px 22px 0 22px}
.post-date{font-size:13px;color:var(--orange);display:flex;align-items:center;gap:5px}
.post-title{font-family:'Roboto',sans-serif;font-weight:500;font-size:17px;line-height:24px;color:var(--ink);margin-top:10px;width:260px}
.post-text{font-size:13px;line-height:22.5px;color:#666;margin-top:14px;width:260px}
.post .btn{position:relative;margin-top:18px;width:146px;height:38px;font-size:13px}
.notch{position:absolute;width:0;height:0;border-left:14px solid transparent;border-right:14px solid transparent}

/* footer */
.footer{position:absolute;left:0;top:3841px;width:1200px;height:469px;background:var(--dark);color:#e6e6e6}
.news-title{position:absolute;left:110px;top:80px;font-family:'Outfit',sans-serif;font-weight:600;font-size:29px;color:var(--white)}
.news-field{position:absolute;left:588px;top:73px;width:498px;height:49px;border-radius:25px;background:var(--white);border:2px solid var(--orange)}
.news-field .ph{position:absolute;left:40px;top:15px;font-size:14px;color:#777}
.news-btn{position:absolute;right:-2px;top:-2px;width:152px;height:49px;border-radius:25px;background:var(--orange);color:var(--white);font-weight:500;font-size:17px;display:flex;align-items:center;justify-content:center}
.footer-rule{position:absolute;left:114px;top:152px;width:972px;height:1px;background:var(--line)}
.f-head{position:absolute;top:202px;font-size:14px;font-weight:700;color:var(--white);text-decoration:underline;text-transform:uppercase}
.vrule{position:absolute;top:212px;width:1px;height:208px;background:var(--line)}
.contact-row{position:absolute;left:114px;display:flex;align-items:flex-start;gap:22px;font-size:14px;line-height:21px;color:#e6e6e6}
.c-ico{width:28px;height:28px;border-radius:50%;background:#2d2d2d;display:flex;align-items:center;justify-content:center;flex:none}
.links{position:absolute;top:238px;list-style:none}
.links li{font-size:14px;height:38px;display:flex;gap:12px;align-items:flex-start;color:#e6e6e6}
.links li::before{content:"»";color:var(--white);font-size:14px}
.bottom-bar{position:absolute;left:0;top:4310px;width:1200px;height:57px;background:var(--orange);color:var(--white);font-size:14px}
.bottom-bar .copy{position:absolute;left:110px;top:20px}
.bottom-socials{position:absolute;left:933px;top:14px;display:flex;gap:10px}
.bottom-socials span{width:30px;height:30px;border-radius:50%;border:1.5px solid var(--white)}
</style>
</head>
<body>

<header class="site-header">
  <div class="brand"><span class="brand-mark"></span><span class="brand-name">LARKMOOR<br>PROPERTIES</span></div>
  <div class="socials"><span class="social"></span><span class="social"></span><span class="social"></span><span class="social"></span></div>
  <div class="top-phone">
    <span class="phone-badge"><svg width="14" height="14" viewBox="0 0 24 24"><path fill="#f26b21" d="M6.6 10.8a15.1 15.1 0 0 0 6.6 6.6l2.2-2.2c.3-.3.7-.4 1-.2 1.1.4 2.3.6 3.6.6.6 0 1 .4 1 1V20c0 .6-.4 1-1 1A17 17 0 0 1 3 4c0-.6.4-1 1-1h3.5c.6 0 1 .4 1 1 0 1.3.2 2.5.6 3.6.1.3 0 .7-.2 1z"/></svg></span>
    +1 555 014 2290
  </div>
  <nav class="nav">
    <a style="left:90px">Home</a><span class="sep" style="left:163px">|</span>
    <a style="left:200px">About Us</a><span class="sep" style="left:300px">|</span>
    <a style="left:337px">Services</a><span class="sep" style="left:435px">|</span>
    <a style="left:476px">Testimonilas</a><span class="sep" style="left:603px">|</span>
    <a style="left:640px">Contact Us</a>
  </nav>
</header>

<section class="hero" role="img" aria-label="Photo of a small model house on a desk beside a person signing a property contract">
  <div class="hero-shade"></div>
  <div class="hero-copy">
    <div class="hero-kicker">WELCOME TO</div>
    <div class="hero-title">LARKMOOR PROPERTIES</div>
    <p class="hero-text">Lorem ipsum dolor sit amet consectetur adipiscing sed eiusmod tempor incididunt labore dolore magna aliqua.</p>
  </div>
  <div class="btn" style="left:580px;top:403px;width:186px;height:43px;font-size:16px">Get Started
    <svg class="arrow" viewBox="0 0 16 16"><circle cx="8" cy="8" r="8" fill="#fff"/><path d="M6.5 4.5 10 8l-3.5 3.5" stroke="#f26b21" stroke-width="2" fill="none"/></svg></div>
</section>

<h2 class="section-title" style="top:860px">OUR <span class="accent">SERVICES</span></h2>

<h3 class="service-title" style="left:112px;top:968px">Property Management<br>Services</h3>
<p class="service-text" style="left:112px;top:1061px;width:415px">Lorem ipsum dolor sit amet, consectetur adipiscing elit, sed do eiusmod tempor incididunt ut labore et dolore magna aliqua. Ut enim ad minim veniam, quis nostrud exercitation ullamco laboris nisi ut aliquip ex ea commodo consequat. Duis aute irure dolor in reprehenderit in voluptate velit esse cillum dolore eu fugiat nulla pariatur. Excepteur sint occaecat cupidatat non proident, sunt in culpa qui officia deserunt mollit anim id est laborumDuis aute irure dolor in reprehenderit in voluptate velit esse cillum.</p>
<div class="btn" style="left:112px;top:1288px;width:171px;height:43px">Read More
  <svg class="arrow" viewBox="0 0 16 16"><circle cx="8" cy="8" r="8" fill="#fff"/><path d="M6.5 4.5 10 8l-3.5 3.5" stroke="#f26b21" stroke-width="2" fill="none"/></svg></div>
<div class="photo" style="left:612px;top:956px;width:476px;height:395px;background:linear-gradient(180deg,#7fb3e4 0%,#c8dced 45%,#a9a296 70%,#6f8f4e 100%)" role="img" aria-label="Photo of modern white apartment buildings along a garden path"></div>
<div class="service-icon" style="left:560px;top:1092px"><span>
  <svg width="48" height="48" viewBox="0 0 48 48" fill="none" stroke="#fff" stroke-width="2.5"><path d="M6 22 24 8l18 14"/><path d="M11 19v21h26V19"/><rect x="20" y="28" width="8" height="12"/><rect x="14" y="24" width="5" height="5"/><rect x="29" y="24" width="5" height="5"/></svg></span></div>

<div class="photo" style="left:112px;top:1442px;width:476px;height:395px;background:linear-gradient(120deg,#c9c3bb 0%,#8a7f74 45%,#3b4653 75%,#bfb4a8 100%)" role="img" aria-label="Photo of a real estate agent showing a laptop to a smiling couple"></div>
<div class="service-icon" style="left:520px;top:1577px"><span>
  <svg width="48" height="48" viewBox="0 0 48 48" fill="none" stroke="#fff" stroke-width="2.5"><path d="M6 22 24 8l18 14"/><path d="M11 19v21h26V19"/><rect x="20" y="28" width="8" height="12"/><rect x="14" y="24" width="5" height="5"/><rect x="29" y="24" width="5" height="5"/></svg></span></div>
<h3 class="service-title" style="left:673px;top:1474px">Real Estate Services</h3>
<p class="service-text" style="left:675px;top:1529px;width:413px">Lorem ipsum dolor sit amet, consectetur adipiscing elit, sed do eiusmod tempor incididunt ut labore et dolore magna aliqua. Ut enim ad minim veniam, quis nostrud exercitation ullamco laboris nisi ut aliquip ex ea commodo consequat. Duis aute irure dolor in reprehenderit in voluptate velit esse cillum dolore eu fugiat nulla pariatur. Excepteur sint occaecat cupidatat non proident, sunt in culpa qui officia deserunt mollit anim id est laborumDuis aute irure dolor in reprehenderit in voluptate velit esse cillum.</p>
<div class="btn" style="left:676px;top:1756px;width:170px;height:42px">Read More
  <svg class="arrow" viewBox="0 0 16 16"><circle cx="8" cy="8" r="8" fill="#fff"/><path d="M6.5 4.5 10 8l-3.5 3.5" stroke="#f26b21" stroke-width="2" fill="none"/></svg></div>

<section class="about">
  <h2 class="heading" style="position:absolute;left:114px;top:93px;font-size:36px">ABOUT <span class="accent">US</span></h2>
  <p class="about-text">Lorem ipsum dolor sit amet, consectetur adipiscing elit, sed do eiusmod tempor incididunt ut labore et dolore magna aliqua. Ut enim ad minim veniam, quis nostrud exercitation ullamco laboris nisi ut aliquip ex ea commodo consequat. Duis aute irure dolor in reprehenderit in voluptate velit esse cillum dolore eu fugiat nulla pariatur. Excepteur sint occaecat cupidatat non proident, sunt in culpa qui officia deserunt mollit anim id est laborumLorem ipsum dolor sit amet, consectetur adipiscing elit, sed do eiusmod tempor incididunt ut labore et dolore magna aliqua. Ut enim ad minim veniam, quis nostrud exercitation ullamco laboris nisi ut aliquip ommodo consequat Duis aute irure dolor reprehenderit.</p>
  <div class="btn" style="left:114px;top:429px;width:161px;height:41px">Learn More
    <svg class="arrow" viewBox="0 0 16 16"><circle cx="8" cy="8" r="8" fill="#fff"/><path d="M6.5 4.5 10 8l-3.5 3.5" stroke="#f26b21" stroke-width="2" fill="none"/></svg></div>
  <div class="circle-photo" style="left:703px;top:77px;width:388px;height:388px;background:linear-gradient(160deg,#b8c9d8 0%,#e6e2dc 45%,#e98b3f 60%,#cfc6bd 100%)" role="img" aria-label="Photo of two hands passing a small orange model house"></div>
  <div class="circle-photo" style="left:716px;top:330px;width:166px;height:166px;background:linear-gradient(180deg,#9cc0e0 0%,#c9c1b5 50%,#6e8f46 100%)" role="img" aria-label="Photo of a large suburban family home with a lawn"></div>
</section>

<section class="testimonials">
  <h2 class="section-title">OUR TESTIMONIALS</h2>
  <div class="t-card" style="left:114px">
    <div class="avatar" role="img" aria-label="Portrait photo of a client"></div>
    <span class="quote-mark" style="left:22px;top:96px">“</span><span class="quote-mark" style="right:22px;top:192px">”</span>
    <p class="t-text">Sed ut perspiciatis unde omnis iste voluptatem accusantium doloremque laudantium, totam rem aperiam,</p>
    <div class="t-name">-Jhon Smith</div>
  </div>
  <div class="t-card" style="left:446px">
    <div class="avatar" role="img" aria-label="Portrait photo of a client"></div>
    <span class="quote-mark" style="left:22px;top:96px">“</span><span class="quote-mark" style="right:22px;top:192px">”</span>
    <p class="t-text">Sed ut perspiciatis unde omnis iste voluptatem accusantium doloremque laudantium, totam rem aperiam,</p>
    <div class="t-name">-Jhon Smith</div>
  </div>
  <div class="t-card" style="left:778px">
    <div class="avatar" role="img" aria-label="Portrait photo of a client"></div>
    <span class="quote-mark" style="left:22px;top:96px">“</span><span class="quote-mark" style="right:22px;top:192px">”</span>
    <p class="t-text">Sed ut perspiciatis unde omnis iste voluptatem accusantium doloremque laudantium, totam rem aperiam,</p>
    <div class="t-name">-Jhon Smith</div>
  </div>
</section>

<h2 class="section-title" style="top:3098px">OUR <span class="accent">BLOG</span></h2>

<div class="blog-grid">
  <article class="post">
    <div class="post-date"><svg width="12" height="12" viewBox="0 0 12 12"><circle cx="6" cy="6" r="5" stroke="#f26b21" stroke-width="1.4" fill="none"/><path d="M6 3v3l2 1.3" stroke="#f26b21" stroke-width="1.4" fill="none"/></svg>03 May, 2023</div>
    <h4 class="post-title">Sed ut perspiciatis unde omnis iste natus error</h4>
    <p class="post-text">Lorem ipsum dolor sit amet, consectetur ncididunt ut labore et dolore magna aliqua. Ut enim ad minim veniam,</p>
    <div class="btn btn-outline">Read More <svg class="arrow" viewBox="0 0 16 16"><circle cx="8" cy="8" r="8" fill="#f26b21"/><path d="M6.5 4.5 10 8l-3.5 3.5" stroke="#fff" stroke-width="2" fill="none"/></svg></div>
    <span class="notch" style="left:148px;bottom:-14px;border-top:14px solid #fff;z-index:2"></span>
  </article>
  <div style="background:linear-gradient(180deg,#5e8fc7 0%,#9bb7cf 40%,#4d6a7f 70%,#7a9a4f 100%)" role="img" aria-label="Photo of a modern glass office building"></div>
  <article class="post">
    <div class="post-date"><svg width="12" height="12" viewBox="0 0 12 12"><circle cx="6" cy="6" r="5" stroke="#f26b21" stroke-width="1.4" fill="none"/><path d="M6 3v3l2 1.3" stroke="#f26b21" stroke-width="1.4" fill="none"/></svg>03 May, 2023</div>
    <h4 class="post-title">Sed ut perspiciatis unde omnis iste natus error</h4>
    <p class="post-text">Lorem ipsum dolor sit amet, consectetur ncididunt ut labore et dolore magna aliqua. Ut enim ad minim veniam,</p>
    <div class="btn btn-outline">Read More <svg class="arrow" viewBox="0 0 16 16"><circle cx="8" cy="8" r="8" fill="#f26b21"/><path d="M6.5 4.5 10 8l-3.5 3.5" stroke="#fff" stroke-width="2" fill="none"/></svg></div>
    <span class="notch" style="left:148px;bottom:-14px;border-top:14px solid #fff;z-index:2"></span>
  </article>
  <div style="background:linear-gradient(135deg,#8a8f97 0%,#d9d3cc 50%,#a08c79 100%)" role="img" aria-label="Photo of hands handing over house keys with a small house keychain"></div>
  <article class="post">
    <div class="post-date"><svg width="12" height="12" viewBox="0 0 12 12"><circle cx="6" cy="6" r="5" stroke="#f26b21" stroke-width="1.4" fill="none"/><path d="M6 3v3l2 1.3" stroke="#f26b21" stroke-width="1.4" fill="none"/></svg>03 May, 2023</div>
    <h4 class="post-title">Sed ut perspiciatis unde omnis iste natus error</h4>
    <p class="post-text">Lorem ipsum dolor sit amet, consectetur ncididunt ut labore et dolore magna aliqua. Ut enim ad minim veniam,</p>
    <div class="btn btn-outline">Read More <svg class="arrow" viewBox="0 0 16 16"><circle cx="8" cy="8" r="8" fill="#f26b21"/><path d="M6.5 4.5 10 8l-3.5 3.5" stroke="#fff" stroke-width="2" fill="none"/></svg></div>
    <span class="notch" style="left:148px;top:-14px;border-bottom:14px solid #fff;z-index:2"></span>
  </article>
  <div style="background:linear-gradient(180deg,#c7dcef 0%,#d8d0c4 45%,#9b8f7c 65%,#6e9447 100%)" role="img" aria-label="Photo of modern apartment buildings with young trees on a lawn"></div>
</div>

<footer class="footer">
  <h3 class="news-title">SIGN UP FOR NEWSLETTER</h3>
  <div class="news-field">
    <svg class="abs" style="left:17px;top:17px" width="14" height="12" viewBox="0 0 14 12"><rect x="1" y="1" width="12" height="10" rx="1" stroke="#f26b21" stroke-width="1.4" fill="none"/><path d="m1 2 6 5 6-5" stroke="#f26b21" stroke-width="1.4" fill="none"/></svg>
    <span class="ph">Enter Your Email</span>
    <span class="news-btn">SUBSCRIBE</span>
  </div>
  <div class="footer-rule"></div>

  <div class="f-head" style="left:114px">Contact Us</div>
  <div class="contact-row" style="top:248px">
    <span class="c-ico"><svg width="10" height="13" viewBox="0 0 10 13"><path d="M5 0a5 5 0 0 0-5 5c0 3.7 5 8 5 8s5-4.3 5-8a5 5 0 0 0-5-5zm0 7a2 2 0 1 1 0-4 2 2 0 0 1 0 4z" fill="#fff"/></svg></span>
    <span>Unit 1, 2perspiciatis unde omnis<br>atus erro United States</span>
  </div>
  <div class="contact-row" style="top:318px">
    <span class="c-ico"><svg width="12" height="10" viewBox="0 0 12 10"><rect x=".7" y=".7" width="10.6" height="8.6" rx="1" stroke="#fff" stroke-width="1.3" fill="none"/><path d="m.7 1.5 5.3 4 5.3-4" stroke="#fff" stroke-width="1.3" fill="none"/></svg></span>
    <span style="padding-top:4px">info@larkmoorproperties.example</span>
  </div>
  <div class="contact-row" style="top:378px;font-size:20px;font-weight:500;color:#fff">
    <span class="c-ico"><svg width="12" height="12" viewBox="0 0 24 24"><path fill="#fff" d="M6.6 10.8a15.1 15.1 0 0 0 6.6 6.6l2.2-2.2c.3-.3.7-.4 1-.2 1.1.4 2.3.6 3.6.6.6 0 1 .4 1 1V20c0 .6-.4 1-1 1A17 17 0 0 1 3 4c0-.6.4-1 1-1h3.5c.6 0 1 .4 1 1 0 1.3.2 2.5.6 3.6.1.3 0 .7-.2 1z"/></svg></span>
    <span style="padding-top:2px">+1 555 014 2290</span>
  </div>

  <div class="vrule" style="left:461px"></div>
  <div class="f-head" style="left:583px">Quick Links</div>
  <ul class="links" style="left:583px">
    <li>Home</li><li>About Us</li><li>Our Services</li><li>Testimonials</li><li>Contact Us</li>
  </ul>

  <div class="vrule" style="left:822px"></div>
  <div class="f-head" style="left:976px">Other Links</div>
  <ul class="links" style="left:976px">
    <li>Contact Us</li><li>FAQ</li><li>Help Service</li><li>Terms Of Use</li><li>Privacy Policy</li>
  </ul>
</footer>

<div class="bottom-bar">
  <span class="copy">© 2023 Larkmoor Properties. All Rights Reserved</span>
  <div class="bottom-socials"><span></span><span></span><span></span><span></span></div>
</div>

</body>
</html>
```